PSD website for property company

Please read the brief thoroughly.

We are looking for a new website for a property group that does property acquisitions, property development and property management.
They buy, build and lease core inner city industrial assets in Sydney, Australia.
They also invest in residential developments.

Site menu
- Home page
- Property – sub menus include – Leasing ; Projects ; Investments ; Property Management
- Capital and finance
- About
- Contact

They like this website
https://www.verlo.com.au/

They want the site to be clean, modern and bold.
They like few colors, even black and white is OK to submit

They have a logo and style guide and useable images here:
http://www.kumet.net/temp/PelorisWeb2019.zip
The zip file is also attached to this project.
We have supplied some images to give you an idea, but we will also require you to provide at least 3 extra images from stock photos.
Use your imagination.

I am expecting a lot of similar designs, so be aware the photos you choose will be really important.
They want really 3 good stock photos used and supplied without charge.
Please not too generic, I repeat the quality of the photos is important.
You may provide several photos (but not in multiple submissions please) and we will choose the best three to be provided.

The winner will be selected on a single home page design and required to provide;
All photos use in original format without charge
A second ‘standard page’ template design based on the winning home page design

```html
<!DOCTYPE html>
<html lang="en">
<head>
<meta charset="utf-8">
<title>Peloris — Property Group</title>
<link href="https://fonts.googleapis.com/css2?family=Jost:wght@400;500;600&display=swap" rel="stylesheet">
<style>
:root{
  --ink:#1a1d3a;
  --text:#2b2e4a;
  --muted:#8a8da3;
  --page:#f6f7fa;
  --band:#6b52fb;
  --accent:#2f4bd3;
  --pink:#ff4fa7;
  --pink-soft:#fdd6e0;
  --violet:#c65bf2;
  --lavender:#dcd7fe;
  --contact:#f1f1f9;
  --white:#ffffff;
}
*{box-sizing:border-box;margin:0;padding:0}
html,body{width:1200px;height:4112px;overflow:hidden}
body{position:relative;background:var(--page);font-family:"Jost",sans-serif;color:var(--text)}
.abs{position:absolute}
a{color:inherit}
.link{font-size:11px;font-weight:600;color:var(--accent);text-decoration:underline}
.band .link{color:var(--white)}

/* header */
.brand{left:188px;top:38px;font-size:18px;font-weight:600;color:var(--ink)}
.nav{top:44px;font-size:12px;color:var(--muted)}
.nav.active{color:var(--accent);font-weight:500}
.nav.active::after{content:"";position:absolute;left:50%;bottom:-8px;width:12px;height:2px;margin-left:-6px;background:var(--accent)}

/* hero */
.hero-title{left:188px;top:210px;font-size:38px;font-weight:500;line-height:46px;color:var(--ink);z-index:2}
.hero-sub{left:188px;top:326px;font-size:12.5px}
.btn{display:flex;height:45px;border:1.5px solid var(--ink);background:var(--white)}
.btn span{flex:1;display:flex;align-items:center;justify-content:center;font-size:12px;font-weight:600;color:var(--ink)}
.btn i{width:45px;background:var(--accent);display:flex;align-items:center;justify-content:center}
.photo{display:block}
.stat{color:var(--white);padding:12px 12px}
.stat b{display:block;font-size:26px;font-weight:400;margin:6px 0 4px}
.stat small{display:block;font-size:11px;line-height:13px;opacity:.85}

/* who */
.card{background:var(--white);box-shadow:0 10px 30px rgba(26,29,58,.08)}
.card h2{font-size:26px;font-weight:500;color:var(--ink);line-height:33px}
.card p{font-size:12px;line-height:19px;margin-top:14px}
.band{left:0;top:1050px;width:1200px;height:1012px;background:var(--band)}

/* projects */
.section-title{font-size:25px;font-weight:500;line-height:33px}
.projects-title{left:188px;top:1286px;color:var(--white)}
.projects-lead{left:188px;top:1340px;width:380px;font-size:12px;line-height:20px;color:var(--white)}
.project{top:1432px;width:256px;color:var(--white)}
.project h3{margin-top:30px;font-size:17px;font-weight:500}
.project p{margin-top:18px;font-size:12px;line-height:20.5px}
.project .link{display:block;margin-top:28px}

/* services */
.services-title{left:188px;top:2200px;color:var(--ink)}
.service{top:2313px;width:256px;height:298px;background:var(--white);padding:0 27px}
.service .icon{width:75px;height:75px;display:flex;align-items:center;justify-content:center}
.service h3{margin-top:38px;font-size:17px;font-weight:500;color:var(--ink)}
.service p{margin-top:18px;font-size:12px;line-height:20.5px}
.service .link{display:block;margin-top:30px}

/* contact */
.contact{left:0;top:3376px;width:1200px;height:736px;background:var(--contact)}
.contact-title{left:273px;top:3444px;color:var(--ink)}
.contact-lead{left:273px;top:3530px;width:340px;font-size:12px;line-height:20px}
.field{background:var(--white);font-size:12px;padding:14px 15px;color:var(--text)}
.footer-brand{left:273px;top:4044px;font-size:18px;font-weight:600;color:var(--ink)}
.footer-link{top:4050px;font-size:11.5px;color:var(--text)}
</style>
</head>
<body>

<header>
  <div class="abs brand">Peloris</div>
  <a class="abs nav active" style="left:608px">Home</a>
  <a class="abs nav" style="left:677px">Property</a>
  <a class="abs nav" style="left:758px">Capital and Finance</a>
  <a class="abs nav" style="left:902px">About</a>
  <a class="abs nav" style="left:970px">Contact</a>
</header>

<section class="hero">
  <div class="abs photo" style="left:557px;top:107px;width:206px;height:388px;background:linear-gradient(160deg,var(--pink-soft) 55%,#e9b860 80%,#b88a3a)" role="img" aria-label="Pale building corner against a pink sky"></div>
  <div class="abs photo" style="left:779px;top:107px;width:314px;height:469px;background:linear-gradient(200deg,var(--lavender) 10%,#f0ede8 40%,#d7a85a 75%,#f2f0ee)" role="img" aria-label="White and gold facade with windows against a lilac sky"></div>
  <h1 class="abs hero-title">Family owned and operated,<br>community orientated</h1>
  <p class="abs hero-sub">Putting 45 years of local experience to work for the Inner West</p>
  <a class="abs btn" style="left:188px;top:380px;width:180px"><span>Get Strated</span><i><svg width="12" height="10" viewBox="0 0 12 10"><path d="M0 5h10M6 1l4 4-4 4" stroke="#fff" stroke-width="1.6" fill="none"/></svg></i></a>
  <div class="abs stat" style="left:665px;top:452px;width:98px;height:124px;background:#f38fd0">
    <svg width="16" height="14" viewBox="0 0 16 14"><path d="M2 13V3l5-2v12M7 6h6v7M1 13h14" stroke="#fff" stroke-width="1.3" fill="none"/></svg>
    <b>12K</b><small>Projects<br>Completed</small>
  </div>
  <div class="abs stat" style="left:779px;top:452px;width:97px;height:124px;background:#6b6ce0">
    <svg width="16" height="16" viewBox="0 0 16 16"><circle cx="8" cy="8" r="6.5" stroke="#fff" stroke-width="1.3" fill="none"/><path d="M5 9.5c1.6 1.8 4.4 1.8 6 0" stroke="#fff" stroke-width="1.3" fill="none"/></svg>
    <b>30K</b><small>Satisfied<br>Family</small>
  </div>
</section>

<div class="abs band"></div>

<section class="who">
  <div class="abs photo" style="left:188px;top:694px;width:489px;height:487px;background:linear-gradient(120deg,#e8e2d6 35%,#5f9fd8 60%,#9dc8ea 80%,#e6dfd2)" role="img" aria-label="Curved white modernist building under a blue sky"></div>
  <div class="abs card" style="left:508px;top:772px;width:502px;height:332px;padding:68px 70px 0 82px">
    <h2>Who are Peloris</h2>
    <p>When Evangelos Peloris first stepped off the boat and on to Australia’s shores, he dreamt of building a long and prosperous life for his family for many generations to come.</p>
    <p>Accustomed to working with his hands, he soon found employment building one of Australia’s most iconic projects, the Alpine Ridge Hydro Scheme.</p>
    <a class="link" style="display:block;margin-top:22px">Learn More</a>
  </div>
</section>

<section class="band-content">
  <h2 class="abs section-title projects-title">Our recent projects</h2>
  <p class="abs projects-lead">Lorem ipsum dolor sit amet, consetetur sadipscing elitr, sed diam nonumy eirmod tempor invidunt ut</p>

  <article class="abs project" style="left:188px">
    <div class="photo" style="height:336px;background:linear-gradient(160deg,#cfe3ef 30%,#a8a39c 60%,#5d5a55)" role="img" aria-label="Angular grey building with horizontal glazing"></div>
    <h3>Mill St – Creative Arts Precinct</h3>
    <p>Lorem ipsum dolor sit amet, consetetur sadipscing elitr, sed diam nonumy eirmod tempor invidunt ut</p>
    <a class="link">Learn More</a>
  </article>
  <article class="abs project" style="left:472px">
    <div class="photo" style="height:336px;background:linear-gradient(180deg,#cfe2ea 25%,#9a7662 50%,#d1907a 80%)" role="img" aria-label="Timber and brick townhouse facade"></div>
    <h3>Harbour Road Precinct</h3>
    <p>Lorem ipsum dolor sit amet, consetetur sadipscing elitr, sed diam nonumy eirmod tempor invidunt ut</p>
    <a class="link">Learn More</a>
  </article>
  <article class="abs project" style="left:755px">
    <div class="photo" style="height:336px;background:linear-gradient(160deg,#3f7fc6 30%,#f3e6c8 55%,#e8d5ac)" role="img" aria-label="Cream gabled house against a deep blue sky"></div>
    <h3>Mill St – Creative Arts Precinct</h3>
    <p>Lorem ipsum dolor sit amet, consetetur sadipscing elitr, sed diam nonumy eirmod tempor invidunt ut</p>
    <a class="link">Learn More</a>
  </article>
  <article class="abs project" style="left:1038px">
    <div class="photo" style="height:336px;background:linear-gradient(100deg,#6aa596 30%,#9fb3b2 60%,#dfe6e6)" role="img" aria-label="Tall glass tower against a teal sky"></div>
    <h3>Harbour Road Precinct</h3>
    <p>Lorem ipsum dolor sit amet, consetetur sadipscing elitr, sed diam nonumy eirmod tempor invidunt ut</p>
    <a class="link">Learn More</a>
  </article>
</section>

<section class="services">
  <h2 class="abs section-title services-title">Services we provided<br>for you is incomparable &amp; best</h2>

  <article class="abs service" style="left:188px">
    <div class="icon" style="background:var(--pink)"><svg width="24" height="22" viewBox="0 0 24 22"><path d="M1 2h4l3 11h12l2-8H7" stroke="#fff" stroke-width="2" fill="none"/><circle cx="9" cy="18" r="2" fill="#fff"/><circle cx="18" cy="18" r="2" fill="#fff"/></svg></div>
    <h3>Property Acquisitions</h3>
    <p>Lorem ipsum dolor sit amet, consetetur sadipscing elitr, sed diam nonumy eirmod tempor</p>
    <a class="link">Learn More</a>
  </article>
  <article class="abs service" style="left:472px;padding-left:22px">
    <div class="icon" style="background:var(--violet)"><svg width="24" height="20" viewBox="0 0 24 20"><path d="M3 19V4l6-3v18M9 8h9v11M1 19h22" stroke="#fff" stroke-width="2" fill="#fff" fill-opacity=".0"/><rect x="4" y="5" width="4" height="14" fill="#fff"/><rect x="10" y="9" width="7" height="10" fill="#fff"/></svg></div>
    <h3>Property Development</h3>
    <p>Lorem ipsum dolor sit amet, consetetur sadipscing elitr, sed diam nonumy eirmod tempor</p>
    <a class="link">Learn More</a>
  </article>
  <article class="abs service" style="left:755px;padding-left:24px">
    <div class="icon" style="background:var(--band)"><svg width="22" height="20" viewBox="0 0 22 20"><path d="M11 1L1 9h3v10h14V9h3z" fill="#fff"/><circle cx="11" cy="12" r="3" fill="var(--band)"/></svg></div>
    <h3>Property Management</h3>
    <p>Lorem ipsum dolor sit amet, consetetur sadipscing elitr, sed diam nonumy eirmod tempor</p>
    <a class="link">Learn More</a>
  </article>
</section>

<section class="history">
  <div class="abs photo" style="left:522px;top:2777px;width:488px;height:487px;background:linear-gradient(180deg,#8eaec2,#6f92aa 60%,#2c3d63)" role="img" aria-label="Smiling woman with red curly hair in a floral dress against a blue brick wall"></div>
  <div class="abs card" style="left:188px;top:2846px;width:503px;height:349px;padding:50px 68px 0 75px">
    <h2>Our history with the<br>community</h2>
    <p style="margin-top:22px">We have been a part of the Inner West community for more than 50 years, and we plan to remain a part of the community for many years to come. We believe in building communities, not just buildings, and delivering local employment opportunities, so business and people can thrive together. Listening to the community – their wants, needs and expectations – drives the way we plan and deliver our projects.</p>
    <a class="link" style="display:block;margin-top:6px">Learn More</a>
  </div>
</section>

<section class="abs contact"></section>
<section class="contact-content">
  <h2 class="abs section-title contact-title">Contact us. We are here to<br>support you.</h2>
  <p class="abs contact-lead">Lorem ipsum dolor sit amet, consetetur sadipscing elitr, sed diam nonumy eirmod tempor</p>
  <div class="abs field" style="left:273px;top:3604px;width:270px;height:45px">Frist name</div>
  <div class="abs field" style="left:554px;top:3600px;width:270px;height:45px">Last name</div>
  <div class="abs field" style="left:273px;top:3660px;width:270px;height:45px">E-mail</div>
  <div class="abs field" style="left:554px;top:3656px;width:270px;height:45px">Phone</div>
  <div class="abs field" style="left:273px;top:3717px;width:551px;height:134px">Massage</div>
  <a class="abs btn" style="left:273px;top:3889px;width:179px"><span>Send Now</span><i><svg width="12" height="10" viewBox="0 0 12 10"><path d="M0 5h10M6 1l4 4-4 4" stroke="#fff" stroke-width="1.6" fill="none"/></svg></i></a>
</section>

<footer>
  <div class="abs footer-brand">Peloris</div>
  <a class="abs footer-link" style="left:391px">Terms &amp; Condition</a>
  <a class="abs footer-link" style="left:525px">Privacy &amp; Policy</a>
  <a class="abs footer-link" style="left:650px">Support</a>
  <span class="abs footer-link" style="right:193px">© Copyright 2019 &nbsp;|&nbsp; All Rights Reserved</span>
</footer>

</body>
</html>
```